M Website

We need a website design for a construction plant company. You may use a combination of our photos and the stock images. See the logo for company colours. It also be of great value to see moving pictures like the ones on the link: https://www.quindellworks.co.za/copy-of-about-us. See our uploaded files for content.

Target Market(s)

Construction

Number of Pages Required

5+ page

```html
<!DOCTYPE html>
<html lang="en">
<head>
<meta charset="utf-8">
<title>Tessaro Logistics and Plant Hire</title>
<link href="https://fonts.googleapis.com/css2?family=Lato:wght@300;400;700;900&display=swap" rel="stylesheet">
<style>
:root{
  --yellow:#f5c21b;
  --yellow-soft:#f8e08a;
  --ink:#2b2b2b;
  --text:#555;
  --muted:#9a9a9a;
  --band:#e7e7e7;
  --panel:#f1f1f1;
  --white:#fff;
  --hero-a:#3a3834;
  --hero-b:#7a6a52;
}
*{box-sizing:border-box;margin:0;padding:0}
html,body{width:1200px;height:4138px;overflow:hidden}
body{font-family:"Lato",sans-serif;color:var(--ink);background:var(--white);position:relative}
.abs{position:absolute}

/* hero */
.hero{left:0;top:0;width:1200px;height:785px;background:linear-gradient(160deg,var(--hero-a) 0%,#4b463e 45%,var(--hero-b) 100%)}
.hero::after{content:"";position:absolute;inset:0;background:rgba(0,0,0,.35)}
.topbar{left:100px;top:14px;width:1000px;height:44px;z-index:2;display:flex;align-items:center;justify-content:space-between;color:var(--white);font-size:11px}
.brand{display:flex;align-items:center;gap:8px;font-weight:900;font-size:22px;color:var(--white)}
.brand-dot{width:14px;height:14px;border-radius:50%;background:var(--yellow)}
.contact-list{display:flex;gap:26px;align-items:center}
.contact-item{display:flex;align-items:center;gap:7px;line-height:1.25}
.nav{left:100px;top:83px;width:1000px;height:77px;background:var(--white);z-index:2;display:flex;align-items:center;justify-content:center;gap:0}
.nav a{font-size:14px;color:var(--ink);text-decoration:none;letter-spacing:.5px;padding:0 37px}
.hero-title{left:0;top:268px;width:1200px;text-align:center;z-index:2;color:var(--white);font-weight:700;font-size:62px;line-height:76px;letter-spacing:-.5px}
.btn{background:var(--yellow);color:var(--ink);font-weight:700;display:flex;align-items:center;justify-content:center}
.hero-btn{left:485px;top:535px;width:230px;height:77px;font-size:30px;z-index:2}

/* quote band */
.quote-band{left:0;top:785px;width:1200px;height:87px;background:var(--band)}
.quote-band p{position:absolute;left:100px;top:29px;font-size:24px;color:#444}
.quote-band .btn{position:absolute;left:930px;top:16px;width:170px;height:55px;font-size:18px;font-weight:400}

/* about */
.about-title{left:100px;top:898px;width:600px;font-size:27px;font-weight:700;line-height:36px}
.about-title .hl{color:var(--yellow)}
.about-text{left:100px;top:988px;width:600px;font-size:13.5px;line-height:27px;color:#444}
.about-photo{left:786px;top:908px;width:314px;height:179px;background:linear-gradient(135deg,#c9d3dc,#8fa0ae 55%,#d8c3a0)}

/* section heads */
.sec-title{font-size:25px;font-weight:700;color:var(--ink)}
.sec-title::after{content:"";display:block;width:120px;height:3px;background:var(--yellow);margin-top:10px}

/* why */
.why-card{width:314px;height:213px;border:2px solid #c9c9c9;background:var(--white);top:1360px}
.why-num{top:1262px;font-size:130px;font-weight:300;color:var(--yellow-soft);line-height:1}
.why-card h3{position:absolute;left:22px;top:38px;font-size:27px;font-weight:400;color:#444}
.why-card p{position:absolute;left:22px;top:76px;width:270px;font-size:12.5px;line-height:29px;color:#c4c4c4}

/* projects */
.projects{left:0;top:1683px;width:1200px;height:677px;background:var(--band)}
.proj{width:314px;height:247px}
.proj-a{background:linear-gradient(180deg,#4f86c6 0%,#8db3dc 40%,#b7a37d 70%,#6f8d4a 100%)}
.proj-b{background:linear-gradient(180deg,#8ab2d8 0%,#a9c5e0 35%,#9c8664 70%,#5f7f3e 100%)}
.proj-c{background:linear-gradient(180deg,#6d9ccc 0%,#9dbcd9 35%,#826a58 70%,#8a9a66 100%)}
.proj-hover{background:linear-gradient(180deg,#f2c84a,#f0bb28)}
.view-btn{left:72px;top:98px;width:170px;height:50px;background:var(--white);color:#333;font-size:18px;display:flex;align-items:center;justify-content:center}

/* services */
.svc{width:190px;top:2525px}
.svc-img{width:190px;height:124px}
.svc h4{font-size:19px;font-weight:400;margin-top:12px;color:#333}
.svc p{font-size:12.5px;line-height:17px;color:#666;margin-top:3px}

/* team */
.team-title{left:0;top:2858px;width:1200px;text-align:center;font-size:40px;font-weight:700}
.team-band{left:0;top:2944px;width:1200px;height:381px;background:var(--panel)}
.member{width:290px;height:165px;background:var(--white)}
.avatar{position:absolute;left:14px;top:18px;width:60px;height:60px;border-radius:50%;background:linear-gradient(180deg,#8a7a6a,#4a3f36)}
.member h5{position:absolute;left:84px;top:22px;font-size:19px;font-weight:400;color:#333}
.member .role{position:absolute;left:84px;top:48px;font-size:12px;color:#666}
.member p{position:absolute;left:14px;top:90px;width:262px;font-size:10.5px;line-height:15px;color:#555}

/* quote form */
.contact-band{left:0;top:3476px;width:1200px;height:524px;background:var(--band)}
.contact-heading{left:100px;top:3575px;font-size:62px;font-weight:700;color:#666}
.contact-sub{left:100px;top:3672px;width:500px;font-size:48px;font-weight:300;line-height:58px;color:#666}
.form{left:656px;top:3508px;width:444px;height:553px;background:var(--white);box-shadow:0 2px 12px rgba(0,0,0,.25)}
.form label{position:absolute;left:40px;font-size:18px;color:#333}
.field{position:absolute;left:40px;width:370px;border:1px solid #999;background:var(--white)}
.form .btn{position:absolute;left:40px;top:454px;width:370px;height:62px;font-size:24px;font-weight:400}
</style>
</head>
<body>

<div class="abs hero" role="img" aria-label="Construction workers on a building site at dusk"></div>

<header class="abs topbar">
  <div class="brand"><span class="brand-dot"></span>Tessaro</div>
  <div class="contact-list">
    <div class="contact-item">
      <svg width="16" height="18" viewBox="0 0 16 18"><path d="M8 1a6 6 0 0 0-6 6c0 4.5 6 10 6 10s6-5.5 6-10a6 6 0 0 0-6-6z" fill="none" stroke="#f5c21b" stroke-width="1.6"/><circle cx="8" cy="7" r="2" fill="#f5c21b"/></svg>
      <span>P.O. Box 4410, Kestrel Park, 1702<br>18 Fernhill Road, Lindfield, Midrand</span>
    </div>
    <div class="contact-item">
      <svg width="16" height="16" viewBox="0 0 16 16"><path d="M3 1l3 3-2 2a10 10 0 0 0 6 6l2-2 3 3-2 2C7 15 1 9 1 3z" fill="none" stroke="#f5c21b" stroke-width="1.5"/></svg>
      <span>+27 (0)10 555 0142</span>
    </div>
    <div class="contact-item">
      <svg width="20" height="14" viewBox="0 0 20 14"><rect x="1" y="1" width="18" height="12" fill="none" stroke="#f5c21b" stroke-width="1.5"/><path d="M1 1l9 7 9-7" fill="none" stroke="#f5c21b" stroke-width="1.5"/></svg>
      <span>info@tessarohire.co.za</span>
    </div>
  </div>
</header>

<nav class="abs nav">
  <a href="#">HOME</a><a href="#">ABOUT</a><a href="#">COMPANY</a><a href="#">OUR SERVICES</a><a href="#">NEWS</a><a href="#">CONTACT</a>
</nav>

<h1 class="abs hero-title">Delivering high quality<br>multidisciplinary engineering<br>and construction projects</h1>
<a class="abs btn hero-btn">Contact us</a>

<section class="abs quote-band">
  <p>Looking for Quality and affordable Constructer for your project ?</p>
  <a class="btn">Get a Quote</a>
</section>

<h2 class="abs about-title">With Over <span class="hl">5+ Years</span> Experience Rest Assured You're in Safe Hands</h2>
<p class="abs about-text">Tessaro Logistics and Plant Hire (Pty) Ltd is a Black Woman owned Construction and Plant Hire company operating mainly from the Tessaro head office in Midrand (Lindfield) Gauteng. Tessaro Logistics and Plant Hire (Pty) Ltd was established in 2014, and has worked in various municipal jurisdictions within South Africa.</p>
<div class="abs about-photo" role="img" aria-label="Two engineers in hard hats reviewing plans on site"></div>

<h2 class="abs sec-title" style="left:100px;top:1203px">Why &nbsp;You Should Choose Us</h2>

<div class="abs why-card" style="left:100px"><h3>Professional</h3><p>Lorem ipsum dolor sit amet, consectetur adipiscing elit. Sed diam nonummy nibh euismod tincidunt ut laoreet dolore.</p></div>
<div class="abs why-card" style="left:442px"><h3>Longevity</h3><p>Lorem ipsum dolor sit amet, consectetur adipiscing elit. Sed diam nonummy nibh euismod tincidunt ut laoreet dolore.</p></div>
<div class="abs why-card" style="left:786px"><h3>Reliability</h3><p>Lorem ipsum dolor sit amet, consectetur adipiscing elit. Sed diam nonummy nibh euismod tincidunt ut laoreet dolore.</p></div>
<div class="abs why-num" style="left:112px">01</div>
<div class="abs why-num" style="left:454px">02</div>
<div class="abs why-num" style="left:798px">03</div>

<section class="abs projects"></section>
<h2 class="abs sec-title" style="left:100px;top:1688px">Our Latest Completed Project</h2>
<div class="abs proj proj-hover" style="left:100px;top:1763px" role="img" aria-label="Completed house project with yellow highlight overlay"><span class="abs view-btn">VIEW PROJECT</span></div>
<div class="abs proj proj-b" style="left:442px;top:1763px" role="img" aria-label="Completed two-storey brick house"></div>
<div class="abs proj proj-c" style="left:786px;top:1763px" role="img" aria-label="Completed stone-faced family house"></div>
<div class="abs proj proj-a" style="left:100px;top:2094px" role="img" aria-label="Completed blue-roofed family home"></div>
<div class="abs proj proj-b" style="left:442px;top:2094px" role="img" aria-label="Completed two-storey brick house"></div>
<div class="abs proj proj-c" style="left:786px;top:2094px" role="img" aria-label="Completed stone-faced family house"></div>

<h2 class="abs sec-title" style="left:100px;top:2453px">Our Best Class Services</h2>
<div class="abs svc" style="left:100px"><div class="svc-img" role="img" aria-label="Paved road stretching to the horizon" style="background:linear-gradient(180deg,#c9ccd1,#8c8f94 55%,#5d5f62)"></div><h4>Roads &amp; Stormwater</h4><p>Road upgrades and rehabilitation<br>Construction of new Paved roads<br>Paving blocks and asphalt laying</p></div>
<div class="abs svc" style="left:378px"><div class="svc-img" role="img" aria-label="Water flowing over a weir" style="background:linear-gradient(180deg,#5a5650,#8d8a83 50%,#3f3c37)"></div><h4>Water</h4><p>Grey water reticulation<br>Potable water reticulation</p></div>
<div class="abs svc" style="left:643px"><div class="svc-img" role="img" aria-label="Modern white housing development" style="background:linear-gradient(180deg,#9fb9d3,#e8ecef 55%,#b8bcc0)"></div><h4>Housing</h4><p>Grey water reticulation<br>Potable water reticulation</p></div>
<div class="abs svc" style="left:910px"><div class="svc-img" role="img" aria-label="Bathroom with modern sanitation fittings" style="background:linear-gradient(180deg,#6b4a36,#8e6a52 55%,#4e3527)"></div><h4>Sanitation</h4><p>Upgrade of infrastructure –<br>Eradication of bucket systems</p></div>

<h2 class="abs team-title">Our Top Class Engineer With Top Class Service</h2>
<section class="abs team-band"></section>

<div class="abs member" style="left:100px;top:2955px"><div class="avatar" role="img" aria-label="Portrait of the managing director"></div><h5>Marcus Rowe</h5><span class="role">Managing Director</span><p>Oversees strategy and structure so each project is planned, resourced and delivered to clients.</p></div>
<div class="abs member" style="left:455px;top:2955px"><div class="avatar" role="img" aria-label="Portrait of the contracts director"></div><h5>Daniel Okafor</h5><span class="role">Contracts Director</span><p>Supports every contract and keeps daily site activity, reporting and documentation well managed.</p></div>
<div class="abs member" style="left:810px;top:2955px"><div class="avatar" role="img" aria-label="Portrait of the estimator"></div><h5>Leah Brennan</h5><span class="role">Estimator</span><p>Prepares accurate costings and quantities so that each tender is clear and competitive.</p></div>
<div class="abs member" style="left:100px;top:3151px"><div class="avatar" role="img" aria-label="Portrait of the managing director"></div><h5>Marcus Rowe</h5><span class="role">Managing Director</span><p>Oversees strategy and structure so each project is planned, resourced and delivered to clients.</p></div>
<div class="abs member" style="left:455px;top:3151px"><div class="avatar" role="img" aria-label="Portrait of the contracts director"></div><h5>Daniel Okafor</h5><span class="role">Contracts Director</span><p>Supports every contract and keeps daily site activity, reporting and documentation well managed.</p></div>
<div class="abs member" style="left:810px;top:3151px"><div class="avatar" role="img" aria-label="Portrait of the estimator"></div><h5>Leah Brennan</h5><span class="role">Estimator</span><p>Prepares accurate costings and quantities so that each tender is clear and competitive.</p></div>

<section class="abs contact-band"></section>
<h2 class="abs contact-heading">Get &nbsp;A Quote</h2>
<p class="abs contact-sub">Have a question?<br>Free quote?<br>Leave us a<br>message</p>

<form class="abs form">
  <label style="top:32px">Name</label>
  <div class="field" style="top:58px;height:54px"></div>
  <label style="top:144px">Email</label>
  <div class="field" style="top:170px;height:54px"></div>
  <label style="top:256px">Message</label>
  <div class="field" style="top:282px;height:136px"></div>
  <a class="btn">SEND MESSAGE</a>
</form>

</body>
</html>
```